High End Clothing Line Needs Stationary Design

We need a stationery design including letterhead and envelopes for a new Christian clothing company called Covenant 9 based out of New York. Our company colors are charcoal gray and silver. The final design needs to be modern, simple, and have a high end look to it.

Industry/Entity Type

Clothing

Font styles to use
Sans Serif

Colors
474747
cfcfcf

Requirements
Must have
• On the top of page in center we would like a dark gray solid box with logo inside in light gray. Name, email, title, phone # must be on bottom of the page.
• Light gray cross will be on black flap of envelope. Entire back flap in dark gray. Eventually logo and cross will be done in silver stamping when project complete.
Nice to have
• Would like to see how just the logo without Covenant 9 looks in middle of letterhead faded in background.

```html
<!DOCTYPE html>
<html lang="en">
<head>
<meta charset="utf-8">
<title>Covenant 9 Stationery</title>
<link rel="stylesheet" href="https://fonts.googleapis.com/css2?family=Cinzel:wght@400&family=Open+Sans:wght@400;600&display=swap">
<style>
  :root {
    --charcoal: #474747;
    --silver: #cfcfcf;
    --paper: #f4f4f4;
    --paper-edge: #e6e6e6;
    --backdrop: #b4b4b4;
    --label: #3a3a3a;
    --rule: #6a6a6a;
  }
  * { box-sizing: border-box; margin: 0; padding: 0; }
  html, body { width: 1200px; height: 700px; overflow: hidden; }
  body { background: var(--backdrop); position: relative; font-family: "Open Sans", sans-serif; }

  .brand-name {
    font-family: "Cinzel", serif;
    font-weight: 400;
    letter-spacing: 1px;
    white-space: nowrap;
  }

  /* Letterhead */
  .letterhead {
    position: absolute; left: 128px; top: 120px; width: 296px; height: 420px;
    background: radial-gradient(circle at 50% 40%, #ffffff, var(--paper) 60%, var(--paper-edge));
  }
  .letterhead__badge {
    position: absolute; left: 50%; top: 6px; transform: translateX(-50%);
    width: 48px; height: 48px; background: var(--charcoal); border-radius: 4px;
    display: flex; align-items: center; justify-content: center;
  }
  .letterhead__badge .brand-name { color: var(--silver); font-size: 7px; letter-spacing: 0.3px; }
  .letterhead__watermark {
    position: absolute; left: 0; right: 0; top: 245px; text-align: center;
    color: var(--silver); font-size: 30px;
  }
  .letterhead__footer {
    position: absolute; left: 0; right: 0; bottom: 10px; height: 42px;
  }
  .pattern-block {
    position: absolute; width: 42px; height: 42px;
    background: linear-gradient(135deg, var(--charcoal), #9a9a9a);
    opacity: 0.75;
  }
  .letterhead__footer .pattern-block--left { left: 4px; bottom: 0; }
  .letterhead__footer .pattern-block--right { right: 4px; bottom: 0; }
  .contact-fields {
    position: absolute; left: 58px; right: 58px; top: 10px;
    display: grid; grid-template-columns: 1fr 1fr; row-gap: 8px; column-gap: 14px;
  }
  .contact-field { display: flex; align-items: flex-end; gap: 6px; font-size: 5px; font-weight: 600; color: var(--label); }
  .contact-field__line { flex: 1; border-bottom: 0.6px solid var(--rule); height: 5px; }

  /* Envelopes */
  .envelope {
    position: absolute; width: 480px; height: 210px;
    background: radial-gradient(circle at 45% 40%, #ffffff, var(--paper) 60%, var(--paper-edge));
  }
  .envelope--back { left: 600px; top: 90px; }
  .envelope--front { left: 605px; top: 370px; }
  .envelope__flap {
    position: absolute; left: 0; top: 0; width: 100%; height: 62px; background: var(--charcoal);
  }
  .envelope__cross { position: absolute; left: 50%; top: 12px; transform: translateX(-50%); }
  .envelope__mark {
    position: absolute; left: 0; right: 0; text-align: center; color: var(--silver);
  }
  .envelope--back .envelope__mark { top: 120px; font-size: 22px; }
  .envelope--front .envelope__mark { top: 95px; font-size: 28px; }
  .envelope .pattern-block { width: 36px; height: 36px; }
  .envelope .pattern-block--left { left: 4px; bottom: 4px; }
  .envelope .pattern-block--right { right: 4px; bottom: 4px; }
  .envelope--back .pattern-block--right { top: 66px; bottom: auto; }
</style>
</head>
<body>

  <section class="letterhead" aria-label="Letterhead">
    <div class="letterhead__badge"><span class="brand-name">Covenant 9</span></div>
    <div class="letterhead__watermark brand-name">Covenant 9</div>
    <div class="letterhead__footer">
      <div class="pattern-block pattern-block--left" role="img" aria-label="Charcoal and silver checker squares"></div>
      <div class="contact-fields">
        <div class="contact-field">Name <span class="contact-field__line"></span></div>
        <div class="contact-field">Title <span class="contact-field__line"></span></div>
        <div class="contact-field">Email <span class="contact-field__line"></span></div>
        <div class="contact-field">Phone <span class="contact-field__line"></span></div>
      </div>
      <div class="pattern-block pattern-block--right" role="img" aria-label="Charcoal and silver checker squares"></div>
    </div>
  </section>

  <section class="envelope envelope--back" aria-label="Envelope back">
    <div class="envelope__flap">
      <svg class="envelope__cross" width="26" height="36" viewBox="0 0 26 36" aria-hidden="true">
        <line x1="13" y1="0" x2="13" y2="36" stroke="#cfcfcf" stroke-width="1.4"/>
        <line x1="0" y1="12" x2="26" y2="12" stroke="#cfcfcf" stroke-width="1.4"/>
      </svg>
    </div>
    <div class="envelope__mark brand-name">Covenant 9</div>
    <div class="pattern-block pattern-block--left" role="img" aria-label="Charcoal and silver checker squares"></div>
    <div class="pattern-block pattern-block--right" role="img" aria-label="Charcoal and silver checker squares"></div>
  </section>

  <section class="envelope envelope--front" aria-label="Envelope front">
    <div class="envelope__mark brand-name">Covenant 9</div>
    <div class="pattern-block pattern-block--left" role="img" aria-label="Charcoal and silver checker squares"></div>
    <div class="pattern-block pattern-block--right" role="img" aria-label="Charcoal and silver checker squares"></div>
  </section>

</body>
</html>
```